HTML Email template look and feel

Hi, we have been sending out various emails to our clients and they have been a mix of anything from plain text to some html emails that were done for us, i am looking to get a nice design and layout for our HTML emails to keep them looking professional and consistent. What I am looking for is an html email template that has a nice edgy but professional look and feel. Ie header and table styling i suppose. Most of the data we send is either in a 2 or 4 column table layout as such.
Table A
Firm A 6
Firm B 124
Firm C 32435
Table B
Firm A 6 Firm D 4546
Firm B 124 Firm E 3545
Firm C 32435 Firm F 44
For some background our website is http://www.quelmarket.com/
and our logo is on there, and i have attached one of the html emails we are currently sending.
Reason: Just wanted to see what comes in over the weekend before we decide

```html
<!DOCTYPE html>
<html lang="en">
<head>
<meta charset="utf-8">
<title>Quel Market – Daily Volume Report</title>
<link rel="stylesheet" href="https://fonts.googleapis.com/css2?family=Open+Sans:wght@400;600;700&family=Arimo:wght@400;700&display=swap">
<style>
  :root {
    --page-bg: #2f2f2f;
    --frame: #111111;
    --brand-blue: #00a3e0;
    --brand-text: #0b9fd8;
    --topbar-bg: #f1f1f1;
    --topbar-line: #dcdcdc;
    --header-bg: #f6f6f6;
    --row-bg: #f5f5f5;
    --row-line: #e0e0e0;
    --muted: #777777;
    --cell-text: #6f6f6f;
    --title-text: #444444;
    --white: #ffffff;
  }
  * { box-sizing: border-box; margin: 0; padding: 0; }
  html, body { width: 1200px; height: 1097px; overflow: hidden; }
  body { background: var(--page-bg); font-family: "Open Sans", Arial, sans-serif; position: relative; }

  .email {
    position: absolute; left: 238px; top: 34px; width: 724px; height: 990px;
    background: var(--white); border: 3px solid var(--frame); border-radius: 7px; overflow: hidden;
  }

  .topbar {
    height: 37px; background: var(--topbar-bg); border-bottom: 1px solid var(--topbar-line);
    display: flex; justify-content: flex-end; align-items: center; gap: 22px; padding-right: 22px;
    font-size: 12px; color: var(--muted);
  }
  .topbar-link { display: flex; align-items: center; gap: 5px; }
  .topbar-link svg { width: 12px; height: 12px; fill: var(--muted); }

  .masthead {
    height: 116px; background: var(--header-bg); border-bottom: 1px solid var(--row-line);
    display: flex; justify-content: space-between; align-items: center; padding: 0 22px 0 26px;
  }
  .brand { display: flex; align-items: center; gap: 12px; color: var(--brand-blue); }
  .brand-mark { width: 30px; height: 30px; background: var(--brand-blue); }
  .brand-name { font-size: 40px; font-weight: 600; letter-spacing: 1px; }
  .issue { text-align: right; color: var(--brand-text); }
  .issue-date { font-size: 21px; line-height: 26px; }
  .issue-volume { font-size: 16px; line-height: 20px; }

  .section-title {
    height: 78px; display: flex; align-items: center; gap: 11px; padding-left: 30px;
    font-size: 13px; font-weight: 700; color: var(--title-text);
  }
  .section-badge {
    width: 31px; height: 31px; border-radius: 50%; background: var(--brand-blue); color: var(--white);
    display: flex; align-items: center; justify-content: center; font-size: 16px; font-weight: 700;
  }

  .volume-table { width: 100%; border-collapse: collapse; font-family: "Arimo", Arial, sans-serif; table-layout: fixed; }
  .volume-table th {
    height: 66px; background: var(--brand-blue); color: var(--white); font-size: 19px; font-weight: 700;
    line-height: 17px; border-left: 1px solid var(--white);
  }
  .volume-table th:first-child { border-left: none; }
  .volume-table td {
    height: 36px; background: var(--row-bg); color: var(--cell-text); font-size: 14px; text-align: center;
    border-left: 1px solid var(--brand-blue);
  }
  .volume-table td:first-child { border-left: none; }

  .sector-block { display: flex; margin-bottom: 18px; font-family: "Arimo", Arial, sans-serif; }
  .sector { flex: 1; }
  .sector + .sector { border-left: 1px solid var(--brand-blue); }
  .sector-name {
    height: 54px; background: var(--brand-blue); color: var(--white); font-size: 19px; font-weight: 700;
    display: flex; align-items: center; justify-content: center;
  }
  .sector + .sector .sector-name { border-left: 1px solid var(--white); margin-left: -1px; }
  .sector-symbols {
    height: 36px; background: var(--row-bg); border-bottom: 1px solid var(--row-line);
    display: flex; align-items: center; justify-content: space-around; color: var(--cell-text); font-size: 14px;
  }
</style>
</head>
<body>
<div class="email">
  <div class="topbar">
    <span class="topbar-link"><svg viewBox="0 0 12 12"><circle cx="6" cy="3.2" r="2.8"/><path d="M1 12c0-3.5 2.2-5.5 5-5.5s5 2 5 5.5z"/></svg>Forward to a friend</span>
    <span class="topbar-link"><svg viewBox="0 0 12 12"><path d="M6 1l6 5h-2v5H7.5V8h-3v3H2V6H0z"/></svg>Online Version</span>
    <span class="topbar-link"><svg viewBox="0 0 12 12"><path d="M2 0h8v12H2zM3.3 1.3v8h5.4v-8z"/></svg>Mobile Version</span>
    <span class="topbar-link"><svg viewBox="0 0 12 12"><path d="M6 0a6 6 0 100 12A6 6 0 006 0zm0 1.8a4.2 4.2 0 013.3 6.8L3.4 2.7A4.2 4.2 0 016 1.8zM2.7 3.4l5.9 5.9A4.2 4.2 0 012.7 3.4z"/></svg>Unsubscribe</span>
  </div>

  <div class="masthead">
    <div class="brand"><span class="brand-mark"></span><span class="brand-name">QUEL MARKET</span></div>
    <div class="issue">
      <div class="issue-date">01 December 2011</div>
      <div class="issue-volume">27,490,544 Shared Executed*</div>
    </div>
  </div>

  <div class="section-title"><span class="section-badge">10</span>Top 10 Symbols As % Of Volume</div>
  <table class="volume-table">
    <thead>
      <tr><th>Symbol</th><th>% of previous<br>day’s volume</th><th>Symbol</th><th>% of previous<br>day’s volume</th></tr>
    </thead>
    <tbody>
      <tr><td>WOLN</td><td>23.84%</td><td>WOLN</td><td>23.84%</td></tr>
      <tr><td>LMRG</td><td>16.71%</td><td>LMRG</td><td>16.71%</td></tr>
      <tr><td>LUVA</td><td>14.61%</td><td>LUVA</td><td>14.61%</td></tr>
      <tr><td>EXRN</td><td>13.27%</td><td>EXRN</td><td>13.27%</td></tr>
      <tr><td>PAKO</td><td>13.27%</td><td>PAKO</td><td>13.27%</td></tr>
    </tbody>
  </table>

  <div class="section-title"><span class="section-badge">5</span>Top 5 by Sector</div>

  <div class="sector-block">
    <div class="sector"><div class="sector-name">Consumer Discretionary</div><div class="sector-symbols"><span>KZT</span><span>SORA</span><span>YAV</span><span>BQR</span><span>MPVA</span></div></div>
    <div class="sector"><div class="sector-name">Industrials</div><div class="sector-symbols"><span>KZT</span><span>SORA</span><span>YAV</span><span>BQR</span><span>MPVA</span></div></div>
  </div>
  <div class="sector-block">
    <div class="sector"><div class="sector-name">Consumer Discretionary</div><div class="sector-symbols"><span>KZT</span><span>SORA</span><span>YAV</span><span>BQR</span><span>MPVA</span></div></div>
    <div class="sector"><div class="sector-name">Industrials</div><div class="sector-symbols"><span>KZT</span><span>SORA</span><span>YAV</span><span>BQR</span><span>MPVA</span></div></div>
  </div>
  <div class="sector-block">
    <div class="sector"><div class="sector-name">Consumer Discretionary</div><div class="sector-symbols"><span>KZT</span><span>SORA</span><span>YAV</span><span>BQR</span><span>MPVA</span></div></div>
    <div class="sector"><div class="sector-name">Industrials</div><div class="sector-symbols"><span>KZT</span><span>SORA</span><span>YAV</span><span>BQR</span><span>MPVA</span></div></div>
  </div>
  <div class="sector-block">
    <div class="sector"><div class="sector-name">Consumer Discretionary</div><div class="sector-symbols"><span>KZT</span><span>SORA</span><span>YAV</span><span>BQR</span><span>MPVA</span></div></div>
    <div class="sector"><div class="sector-name">Industrials</div><div class="sector-symbols"><span>KZT</span><span>SORA</span><span>YAV</span><span>BQR</span><span>MPVA</span></div></div>
  </div>
</div>
</body>
</html>
```